Creative - Appealing - Business Card Design Project

Looking for a Business card design (vector artwork) for an existing company called 'Fernway Sound'. We operate in the entertainment industry specializing in audio system design and rental, however; we also deal with other sectors of the entertainment industry including lighting, video, staging and power system design and rental. We would like to see designs that don't focus too much on audio but include elements encompassing everything else.

Double sided business card, following our new colour scheme and logo, which is attached. The card would ideally be creative and eye catching to draw in new customers in the elegant event production market, such as weddings & corporate affairs.

Target Market(s)

High end corporate clients, wedding clients

Industry/Entity Type

Entertainment

Requirements
Must have
• Our contact details, these can be worded & listed however you think appropriate as part as the design

Business Name - Fernway Sound
My Name - Dominic Harwell
Web Address - www.fernwaysound-example.com
Mobile Number - 07914 362 517
Office Number - 0330 481 7265
Email - dom@fernwaysound-example.com

The name, email and mobile number would need to be able to be changed to my business partners also.

The font used on our logo is Sansation
Nice to have
• On one side maybe a word cloud involving the services in which we can provide; Lighting, Sound, Event Production, Staging, LED Uplighting, Projection Mapping, Wedding Hire

On the other side, all the important credentials of contact.
Should not have
• The design should not use any old style fonts (i.e Times New Roman, Gothic etc) or on the other side of the scale, any 'jokey' fonts (i.e. Comic Sans).

The font to be used is Sansation

```html
<!DOCTYPE html>
<html lang="en">
<head>
<meta charset="utf-8">
<title>Fernway Sound – Business Card</title>
<link rel="stylesheet" href="https://fonts.googleapis.com/css2?family=Exo+2:wght@400;500;600;700&display=swap">
<style>
  :root {
    --page-bg: #e9e9e9;
    --purple-deep: #4b2a86;
    --purple-mid: #6a45a8;
    --purple-light: #8f72c4;
    --purple-text: #8a6fc9;
    --brand-purple: #5b3a93;
    --ink-black: #0d0d0d;
    --white: #ffffff;
    --soft-grey: #c9c9c9;
    --card-shadow: 0 18px 40px rgba(0,0,0,0.28);
  }
  * { margin: 0; padding: 0; box-sizing: border-box; }
  html, body {
    width: 1200px; height: 1016px; overflow: hidden;
    background: var(--page-bg);
    font-family: "Exo 2", sans-serif;
  }
  .sheet { position: relative; width: 1200px; height: 1016px; }

  .card {
    position: absolute; left: 280px;
    width: 640px; height: 366px;
    box-shadow: var(--card-shadow);
    overflow: hidden;
  }
  .card-front { top: 90px; }
  .card-back  { top: 540px; }

  .card-art { position: absolute; inset: 0; width: 100%; height: 100%; }

  /* front */
  .front-content {
    position: absolute; inset: 0;
    display: flex; flex-direction: column; align-items: center; justify-content: center;
    color: var(--white); text-align: center;
    padding-top: 10px;
  }
  .front-brand {
    display: flex; align-items: center; gap: 14px;
    font-size: 50px; font-weight: 700; letter-spacing: 1px; line-height: 1;
  }
  .brand-dot { width: 22px; height: 22px; border-radius: 50%; background: var(--white); flex: none; }
  .services {
    margin-top: 34px;
    font-size: 16px; font-weight: 500; line-height: 1.35; letter-spacing: 0.3px;
  }
  .front-web { margin-top: 12px; font-size: 12px; letter-spacing: 0.4px; opacity: 0.95; }

  /* back */
  .back-brand {
    position: absolute; left: 36px; top: 118px; width: 200px;
    display: flex; flex-direction: column; align-items: center; gap: 10px;
    color: var(--brand-purple); text-align: center;
  }
  .back-brand .brand-dot { width: 18px; height: 18px; background: var(--brand-purple); }
  .back-brand-name {
    font-size: 38px; font-weight: 700; line-height: 1.05; letter-spacing: 0.5px;
  }
  .person {
    position: absolute; right: 34px; top: 30px; text-align: right;
  }
  .person-name { font-size: 24px; font-weight: 700; color: var(--purple-text); }
  .person-title { margin-top: 4px; font-size: 15px; color: var(--soft-grey); }

  .contacts {
    position: absolute; right: 30px; top: 182px;
    list-style: none; color: var(--white);
    font-size: 15px; letter-spacing: 0.3px;
  }
  .contacts li { display: flex; align-items: center; gap: 9px; line-height: 1.5; }
  .contacts li.gap { margin-top: 16px; }
  .icon { width: 15px; height: 15px; flex: none; }
</style>
</head>
<body>
<main class="sheet">

  <section class="card card-front" aria-label="Business card front">
    <svg class="card-art" viewBox="0 0 640 366" preserveAspectRatio="none" aria-hidden="true">
      <defs>
        <linearGradient id="frontGrad" x1="0" y1="1" x2="1" y2="0">
          <stop offset="0" stop-color="#4a2884"/>
          <stop offset="0.6" stop-color="#6a45a8"/>
          <stop offset="1" stop-color="#9d86cc"/>
        </linearGradient>
      </defs>
      <rect width="640" height="366" fill="url(#frontGrad)"/>
      <polygon points="0,120 210,70 330,366 0,366" fill="#3f2275" opacity="0.45"/>
      <polygon points="150,160 340,110 250,366" fill="#5a389a" opacity="0.55"/>
      <polygon points="330,120 640,20 470,250" fill="#7b5cb7" opacity="0.4"/>
      <polygon points="0,0 260,0 120,130" fill="#8a6cc2" opacity="0.25"/>
    </svg>
    <div class="front-content">
      <div class="front-brand"><span class="brand-dot"></span>Fernway Sound</div>
      <p class="services">Lighting | Sound | Event Production | Staging,<br>LED Uplighting | Projection Mapping | Wedding Hire</p>
      <p class="front-web">www.fernwaysound-example.com</p>
    </div>
  </section>

  <section class="card card-back" aria-label="Business card back">
    <svg class="card-art" viewBox="0 0 640 366" preserveAspectRatio="none" aria-hidden="true">
      <defs>
        <radialGradient id="backGrad" cx="0.6" cy="0.35" r="0.7">
          <stop offset="0" stop-color="#3a3a3a"/>
          <stop offset="1" stop-color="#070707"/>
        </radialGradient>
        <linearGradient id="wedgeGrad" x1="0" y1="0" x2="0" y2="1">
          <stop offset="0" stop-color="#8a6cc2"/>
          <stop offset="1" stop-color="#4a2884"/>
        </linearGradient>
      </defs>
      <rect width="640" height="366" fill="url(#backGrad)"/>
      <polygon points="0,0 300,0 340,366 0,366" fill="url(#wedgeGrad)"/>
      <polygon points="0,0 235,0 335,366 0,366" fill="#ffffff"/>
    </svg>

    <div class="back-brand">
      <span class="brand-dot"></span>
      <p class="back-brand-name">Fernway<br>Sound</p>
    </div>

    <div class="person">
      <p class="person-name">Dominic Harwell</p>
      <p class="person-title">Job Title</p>
    </div>

    <ul class="contacts">
      <li>
        <svg class="icon" viewBox="0 0 16 16" aria-hidden="true"><rect x="4" y="1" width="8" height="14" rx="1.5" fill="none" stroke="#8a6fc9" stroke-width="1.6"/><circle cx="8" cy="12.5" r="0.9" fill="#8a6fc9"/></svg>
        07914 362 517
      </li>
      <li>
        <svg class="icon" viewBox="0 0 16 16" aria-hidden="true"><path d="M3 2 L6 2 L7 5 L5.5 6.5 Q7 9.5 9.5 10.5 L11 9 L14 10 L14 13 Q8 14 2.5 8 Q2 5 3 2 Z" fill="#8a6fc9"/></svg>
        0330 481 7265
      </li>
      <li class="gap">
        <svg class="icon" viewBox="0 0 16 16" aria-hidden="true"><rect x="1" y="3" width="14" height="10" fill="#8a6fc9"/><path d="M1 3 L8 9 L15 3" fill="none" stroke="#1a1a1a" stroke-width="1.2"/></svg>
        dom@fernwaysound-example.com
      </li>
      <li>
        <svg class="icon" viewBox="0 0 16 16" aria-hidden="true"><circle cx="8" cy="8" r="6.5" fill="none" stroke="#8a6fc9" stroke-width="1.5"/><ellipse cx="8" cy="8" rx="3" ry="6.5" fill="none" stroke="#8a6fc9" stroke-width="1.2"/><line x1="1.5" y1="8" x2="14.5" y2="8" stroke="#8a6fc9" stroke-width="1.2"/></svg>
        www.fernwaysound-example.com
      </li>
    </ul>
  </section>

</main>
</body>
</html>
```